Single Page Timetracking Dashboard Desktop App UI Design (Figma Link required)

Main Idea: a SaaS tool where employees can add their time and project in a playful way. There is a infographics and a list with tasks as well.

Based on the attached concept.png the brief is following:

- check the attached rough scribble
- add own ideas or change things if they add value
- Style: colourful, nerdy, professional saas, modern, beautiful, white space
- Quality expectation: inspiration1+2.png
- I will need a Figma link
- desktop only
- make something fresh and unique

Process:
I need to include 2-3 feedback rounds that will span probably around 7 days

Target Market(s)

Internal Business Tool for a Software Development Company

Industry/Entity Type

IT

Other font styles liked:
• Could be monospace, not a must though

Requirements
Must have
• At least one page; Figma Link to the design;
Nice to have
• Microinterations like drop-down, hover/active colors; functionality specifications
Should not have
• Mobile view

```html
<!DOCTYPE html>
<html lang="en">
<head>
<meta charset="utf-8">
<title>Time Tracking Dashboard</title>
<link href="https://fonts.googleapis.com/css2?family=Inter:wght@400;500;600;700&display=swap" rel="stylesheet">
<style>
:root{
  --bg:#f4f4f5;
  --surface:#ffffff;
  --line:#e6e8ec;
  --ink:#15171c;
  --muted:#8b909a;
  --blue:#1f73f1;
  --blue-soft:#eaf2fe;
  --row:#f1f5fd;
  --orange:#f7a240;
  --green:#1aa33f;
  --sky:#1aa4f0;
  --red:#e5262a;
  --tag-bg:#e6f7ea;
  --tag-ink:#1f9a3d;
}
*{box-sizing:border-box;margin:0;padding:0}
html,body{width:1200px;height:1200px;overflow:hidden}
body{background:var(--bg);font-family:"Inter",sans-serif;color:var(--ink)}
.screen{position:relative;width:1200px;height:600px;display:flex;background:var(--bg);border-bottom:1px solid var(--line)}
.sidebar{width:72px;background:var(--surface);border-right:1px solid var(--line);display:flex;flex-direction:column;align-items:center;padding-top:14px;gap:14px}
.brand{display:flex;align-items:center;gap:5px;color:var(--blue);font-weight:600;font-size:12px;margin-bottom:8px}
.brand-dot{width:10px;height:10px;border:2px solid var(--blue);border-radius:50%}
.side-item{display:flex;flex-direction:column;align-items:center;gap:4px;font-size:9px;color:var(--muted)}
.side-item.active{color:var(--ink)}
.side-icon{width:34px;height:34px;border-radius:9px;background:#f1f2f4;display:flex;align-items:center;justify-content:center}
.side-item.active .side-icon{background:var(--blue);box-shadow:0 4px 10px rgba(31,115,241,.35)}
.main{flex:1;display:flex;flex-direction:column}
.topbar{height:52px;background:var(--surface);border-bottom:1px solid var(--line);display:flex;align-items:center;justify-content:center;gap:34px;position:relative;font-size:12px}
.nav-link{display:flex;align-items:center;gap:6px}
.topbar-right{position:absolute;right:24px;display:flex;gap:16px;align-items:center}
.bell{position:relative}
.bell::after{content:"";position:absolute;top:0;right:0;width:5px;height:5px;border-radius:50%;background:var(--red)}
.avatar{width:24px;height:24px;border-radius:50%;background:linear-gradient(135deg,#e9b58c,#b9673d)}
.content{padding:14px 22px;display:flex;flex-direction:column;gap:12px}
.card{background:var(--surface);border:1px solid var(--line);border-radius:10px;padding:12px 16px}
.card-title{font-size:19px;font-weight:600;margin-bottom:10px}
/* track */
.track{display:grid;grid-template-columns:250px 230px 1fr;grid-template-rows:auto auto;column-gap:14px;row-gap:8px}
.calendar{border:1px solid var(--line);border-radius:8px;padding:6px 10px;font-size:8px}
.cal-head{display:flex;justify-content:space-between;font-size:10px;font-weight:500;margin-bottom:4px}
.cal-grid{display:grid;grid-template-columns:repeat(7,1fr);row-gap:2px;text-align:center}
.cal-grid .wd{color:var(--muted);font-size:7px}
.cal-grid span{height:15px;line-height:15px}
.cal-grid .dim{color:var(--muted)}
.cal-grid .sel{background:var(--blue);color:#fff;border-radius:50%;width:15px;margin:0 auto}
.selects{display:flex;flex-direction:column;gap:6px}
.select{border:1px solid var(--line);border-radius:6px;height:24px;padding:0 8px;display:flex;justify-content:space-between;align-items:center;font-size:9px}
.options{border:1px solid var(--line);border-radius:6px;padding:6px 8px;display:flex;flex-direction:column;gap:4px;font-size:9px}
.options a{color:var(--blue)}
.hours{border:1px solid var(--line);border-radius:8px;padding:8px;display:grid;grid-template-columns:repeat(4,1fr);gap:6px;align-content:start}
.chip{height:26px;border:1px solid var(--line);border-radius:6px;display:flex;align-items:center;justify-content:center;font-size:11px;box-shadow:0 1px 3px rgba(0,0,0,.05)}
.chip.on{border-color:var(--blue);box-shadow:0 0 0 1px var(--blue)}
.and{grid-column:1/-1;text-align:center;font-size:7px;color:var(--muted);border-top:1px solid var(--line);padding-top:2px;height:10px}
.note{grid-column:1/3;border:1px solid var(--line);border-radius:8px;height:52px;padding:8px 10px;font-size:9px;color:var(--muted)}
.submit{display:flex;align-items:center;gap:12px}
.total{flex:1;border:1px solid var(--line);border-radius:8px;height:40px;display:flex;align-items:center;padding:0 12px;font-size:13px;font-weight:600}
.btn{background:var(--blue);color:#fff;border-radius:6px;padding:8px 22px;font-size:11px;font-weight:500;box-shadow:0 4px 10px rgba(31,115,241,.3)}
/* stats */
.stats-head{display:flex;justify-content:space-between;align-items:center;margin-bottom:8px}
.stats-head .card-title{margin:0}
.dropdown{border:1px solid var(--line);border-radius:6px;padding:5px 10px;font-size:9px;display:flex;gap:14px;align-items:center}
.stats-grid{display:grid;grid-template-columns:1fr 1fr;gap:14px}
.stat{border:1px solid var(--line);border-radius:8px;padding:10px 14px;display:grid;grid-template-columns:150px 1fr;grid-template-rows:auto 1fr;column-gap:16px}
.stat-head{grid-column:1/-1;display:flex;justify-content:space-between;align-items:center;font-size:12px;font-weight:600;margin-bottom:4px}
.pill{border:1px solid var(--line);border-radius:5px;padding:3px 8px;font-size:9px;font-weight:500}
.legend{display:flex;flex-direction:column;gap:5px;font-size:10px;font-weight:500;justify-content:center}
.legend li{list-style:none;display:flex;gap:6px}
.legend i{width:5px;height:5px;border-radius:1px;margin-top:4px}
.legend small{display:block;font-size:8px;color:var(--muted);font-weight:400}
.donut{width:130px;height:130px}
/* tasks */
.tasks-card{flex:1}
.day{margin-bottom:8px}
.day-head{display:flex;justify-content:space-between;align-items:flex-end;font-size:13px;font-weight:600;margin-bottom:5px}
.day-head small{font-size:9px;font-weight:600}
.task{background:var(--row);border-radius:8px;padding:7px 12px;display:flex;justify-content:space-between;margin-bottom:6px}
.tag{display:inline-block;background:var(--tag-bg);color:var(--tag-ink);font-size:8px;padding:2px 6px;border-radius:4px;margin-bottom:3px}
.task-name{font-size:13px;font-weight:600}
.task-desc{font-size:9px;color:#4c515b}
.task-side{text-align:right;display:flex;flex-direction:column;justify-content:space-between}
.actions{font-size:9px;display:flex;gap:10px;justify-content:flex-end}
.edit{color:var(--blue)}
.delete{color:var(--red)}
.dur{font-size:13px;font-weight:600}
.date{font-size:9px;color:var(--muted)}
</style>
</head>
<body>

<section class="screen">
  <aside class="sidebar">
    <div class="brand"><span class="brand-dot"></span>Logo</div>
    <div class="side-item active"><div class="side-icon"><svg width="16" height="16" viewBox="0 0 24 24" fill="none" stroke="#fff" stroke-width="2"><circle cx="12" cy="13" r="8"/><path d="M12 9v4M9 2h6"/></svg></div>Clock</div>
    <div class="side-item"><div class="side-icon"><svg width="14" height="14" viewBox="0 0 24 24" fill="#6b707a"><rect x="3" y="3" width="18" height="18" rx="3"/><path d="M8 16v-4M12 16V8M16 16v-6" stroke="#fff" stroke-width="2"/></svg></div>Statistics</div>
    <div class="side-item"><div class="side-icon"><svg width="14" height="14" viewBox="0 0 24 24" fill="none" stroke="#3b3f47" stroke-width="2"><rect x="3" y="4" width="18" height="16" rx="2"/><path d="M3 14h5l2 3h4l2-3h5"/></svg></div>Task</div>
    <div class="side-item"><div class="side-icon"><svg width="14" height="14" viewBox="0 0 24 24" fill="#6b707a"><circle cx="10" cy="8" r="4"/><path d="M2 20c0-4 4-6 8-6s8 2 8 6z"/></svg></div>User</div>
  </aside>
  <div class="main">
    <header class="topbar">
      <span class="nav-link"><svg width="13" height="13" viewBox="0 0 24 24" fill="none" stroke="#3b3f47" stroke-width="2"><rect x="3" y="7" width="18" height="13" rx="2"/><path d="M9 7V4h6v3"/></svg>Projects</span>
      <span class="nav-link"><svg width="13" height="13" viewBox="0 0 24 24" fill="none" stroke="#3b3f47" stroke-width="2"><rect x="4" y="3" width="16" height="18"/><path d="M8 7h2M14 7h2M8 11h2M14 11h2M8 15h2M14 15h2"/></svg>Clients</span>
      <span class="nav-link"><svg width="13" height="13" viewBox="0 0 24 24" fill="none" stroke="#3b3f47" stroke-width="2"><rect x="2" y="6" width="20" height="12" rx="2"/><circle cx="12" cy="12" r="3"/></svg>Salaries</span>
      <span class="nav-link"><svg width="13" height="13" viewBox="0 0 24 24" fill="#3b3f47"><rect x="3" y="3" width="18" height="18" rx="3"/><circle cx="12" cy="10" r="3" fill="#fff"/><path d="M7 18c1-3 9-3 10 0" fill="#fff"/></svg>Careers</span>
      <div class="topbar-right">
        <span class="bell"><svg width="14" height="14" viewBox="0 0 24 24" fill="#6b707a"><path d="M6 17V11a6 6 0 0112 0v6l2 2H4z"/><circle cx="12" cy="21" r="2"/></svg></span>
        <div class="avatar" role="img" aria-label="User profile photo"></div>
      </div>
    </header>
    <div class="content">
      <div class="card">
        <h1 class="card-title">Track your time</h1>
        <div class="track">
          <div class="calendar">
            <div class="cal-head"><span>◂</span>October 2023<span>▸</span></div>
            <div class="cal-grid">
              <span class="wd">Mon</span><span class="wd">Tue</span><span class="wd">Wed</span><span class="wd">Thu</span><span class="wd">Fri</span><span class="wd">Sat</span><span class="wd">Sun</span>
              <span class="dim">28</span><span class="dim">29</span><span class="dim">30</span><span class="dim">31</span><span>1</span><span>2</span><span>3</span>
              <span>4</span><span>5</span><span>6</span><span>7</span><span>8</span><span>9</span><span>10</span>
              <span>11</span><span>12</span><span>13</span><span>14</span><span>15</span><span>16</span><span>17</span>
              <span>18</span><span>19</span><span class="sel">20</span><span>21</span><span>22</span><span>23</span><span>24</span>
              <span>25</span><span>26</span><span>27</span><span>28</span><span>29</span><span>30</span><span>31</span>
              <span class="dim">1</span><span class="dim">2</span><span class="dim">3</span><span class="dim">4</span><span class="dim">5</span><span class="dim">6</span><span class="dim">7</span>
            </div>
          </div>
          <div class="selects">
            <div class="select">Select Project <span>▾</span></div>
            <div class="select">Select Project <span>▾</span></div>
            <div class="options">
              <a>Customer 1 Project 1</a>
              <a>Customer 2 Project 2</a>
              <a>Customer 1 Project 2</a>
              <a>Customer with long name and project name</a>
            </div>
          </div>
          <div class="hours">
            <span class="chip on">1h</span><span class="chip">2h</span><span class="chip">3h</span><span class="chip">4h</span>
            <span class="chip">5h</span><span class="chip">6h</span><span class="chip">7h</span><span class="chip">8h</span>
            <span class="and">And</span>
            <span class="chip">0m</span><span class="chip on">15m</span><span class="chip">30m</span><span class="chip">45m</span>
          </div>
          <div class="note">What did you do?</div>
          <div class="submit"><div class="total">1h 15m</div><span class="btn">Save</span></div>
        </div>
      </div>
      <div class="card">
        <div class="stats-head"><h2 class="card-title">Statistics</h2><span class="dropdown">This Month <span>▾</span></span></div>
        <div class="stats-grid">
          <div class="stat">
            <div class="stat-head">Current Month <span class="pill">Total: 50:45 h</span></div>
            <svg class="donut" viewBox="0 0 130 130">
              <g transform="rotate(-90 65 65)" fill="none">
                <circle cx="65" cy="65" r="40" stroke="#e7effc" stroke-width="26"/>
                <circle cx="65" cy="65" r="58" stroke="var(--sky)" stroke-width="5" stroke-dasharray="82 282"/>
                <circle cx="65" cy="65" r="58" stroke="var(--orange)" stroke-width="5" stroke-dasharray="86 278" stroke-dashoffset="-86"/>
                <circle cx="65" cy="65" r="58" stroke="var(--green)" stroke-width="5" stroke-dasharray="96 268" stroke-dashoffset="-176"/>
                <circle cx="65" cy="65" r="58" stroke="var(--blue)" stroke-width="5" stroke-dasharray="86 278" stroke-dashoffset="-276"/>
              </g>
              <circle cx="65" cy="65" r="24" fill="#fff"/>
              <circle cx="65" cy="65" r="13" fill="#2a2d33" role="img" aria-label="Small reading figure illustration"/>
            </svg>
            <ul class="legend">
              <li><i style="background:var(--blue)"></i><div>40:45 h<small>Customer A (60%)</small></div></li>
              <li><i style="background:var(--orange)"></i><div>10:00 h<small>Customer B (20%)</small></div></li>
              <li><i style="background:var(--green)"></i><div>02:00 h<small>Customer C (20%)</small></div></li>
              <li><i style="background:var(--sky)"></i><div>03:00 h<small>Customer D (20%)</small></div></li>
            </ul>
          </div>
          <div class="stat">
            <div class="stat-head">September <span class="pill">Gasamt: 114:00 h</span></div>
            <svg class="donut" viewBox="0 0 130 130">
              <g transform="rotate(-90 65 65)" fill="none">
                <circle cx="65" cy="65" r="40" stroke="#e7effc" stroke-width="26"/>
                <circle cx="65" cy="65" r="58" stroke="var(--sky)" stroke-width="5" stroke-dasharray="82 282"/>
                <circle cx="65" cy="65" r="58" stroke="var(--orange)" stroke-width="5" stroke-dasharray="86 278" stroke-dashoffset="-86"/>
                <circle cx="65" cy="65" r="58" stroke="var(--green)" stroke-width="5" stroke-dasharray="96 268" stroke-dashoffset="-176"/>
                <circle cx="65" cy="65" r="58" stroke="var(--blue)" stroke-width="5" stroke-dasharray="86 278" stroke-dashoffset="-276"/>
              </g>
              <circle cx="65" cy="65" r="24" fill="#fff"/>
              <circle cx="65" cy="65" r="13" fill="#2a2d33" role="img" aria-label="Small reading figure illustration"/>
            </svg>
            <ul class="legend">
              <li><i style="background:var(--blue)"></i><div>40:45 h<small>Customer A (60%)</small></div></li>
              <li><i style="background:var(--orange)"></i><div>10:00 h<small>Customer B (20%)</small></div></li>
              <li><i style="background:var(--green)"></i><div>02:00 h<small>Customer C (20%)</small></div></li>
              <li><i style="background:var(--sky)"></i><div>03:00 h<small>Customer D (20%)</small></div></li>
            </ul>
          </div>
        </div>
      </div>
    </div>
  </div>
</section>

<section class="screen">
  <aside class="sidebar">
    <div class="brand"><span class="brand-dot"></span>Logo</div>
    <div class="side-item active"><div class="side-icon"><svg width="16" height="16" viewBox="0 0 24 24" fill="none" stroke="#fff" stroke-width="2"><circle cx="12" cy="13" r="8"/><path d="M12 9v4M9 2h6"/></svg></div>Clock</div>
    <div class="side-item"><div class="side-icon"><svg width="14" height="14" viewBox="0 0 24 24" fill="#6b707a"><rect x="3" y="3" width="18" height="18" rx="3"/><path d="M8 16v-4M12 16V8M16 16v-6" stroke="#fff" stroke-width="2"/></svg></div>Statistics</div>
    <div class="side-item"><div class="side-icon"><svg width="14" height="14" viewBox="0 0 24 24" fill="none" stroke="#3b3f47" stroke-width="2"><rect x="3" y="4" width="18" height="16" rx="2"/><path d="M3 14h5l2 3h4l2-3h5"/></svg></div>Task</div>
    <div class="side-item"><div class="side-icon"><svg width="14" height="14" viewBox="0 0 24 24" fill="#6b707a"><circle cx="10" cy="8" r="4"/><path d="M2 20c0-4 4-6 8-6s8 2 8 6z"/></svg></div>User</div>
  </aside>
  <div class="main">
    <header class="topbar">
      <span class="nav-link"><svg width="13" height="13" viewBox="0 0 24 24" fill="none" stroke="#3b3f47" stroke-width="2"><rect x="3" y="7" width="18" height="13" rx="2"/><path d="M9 7V4h6v3"/></svg>Projects</span>
      <span class="nav-link"><svg width="13" height="13" viewBox="0 0 24 24" fill="none" stroke="#3b3f47" stroke-width="2"><rect x="4" y="3" width="16" height="18"/><path d="M8 7h2M14 7h2M8 11h2M14 11h2M8 15h2M14 15h2"/></svg>Clients</span>
      <span class="nav-link"><svg width="13" height="13" viewBox="0 0 24 24" fill="none" stroke="#3b3f47" stroke-width="2"><rect x="2" y="6" width="20" height="12" rx="2"/><circle cx="12" cy="12" r="3"/></svg>Salaries</span>
      <span class="nav-link"><svg width="13" height="13" viewBox="0 0 24 24" fill="#3b3f47"><rect x="3" y="3" width="18" height="18" rx="3"/><circle cx="12" cy="10" r="3" fill="#fff"/><path d="M7 18c1-3 9-3 10 0" fill="#fff"/></svg>Careers</span>
      <div class="topbar-right">
        <span class="bell"><svg width="14" height="14" viewBox="0 0 24 24" fill="#6b707a"><path d="M6 17V11a6 6 0 0112 0v6l2 2H4z"/><circle cx="12" cy="21" r="2"/></svg></span>
        <div class="avatar" role="img" aria-label="User profile photo"></div>
      </div>
    </header>
    <div class="content">
      <div class="card tasks-card">
        <div class="stats-head"><h1 class="card-title">Your Tasks</h1><span class="dropdown">This Month <span>▾</span></span></div>

        <div class="day">
          <div class="day-head">Wednesday <small>7H 30M</small></div>
          <div class="task">
            <div><span class="tag">Coding</span><div class="task-name">Customer A Project 1</div><div class="task-desc">It tracks your progress from first until now</div></div>
            <div class="task-side"><div class="actions"><span class="edit">✎ Edit</span><span class="delete">■ Delete</span></div><div class="dur">4h 30m</div><div class="date">December 9th</div></div>
          </div>
        </div>

        <div class="day">
          <div class="day-head">Tuesday <small>7H 30M</small></div>
          <div class="task">
            <div><span class="tag">Project Management</span><div class="task-name">Customer B Project 1</div><div class="task-desc">It tracks your progress from first until now</div></div>
            <div class="task-side"><div class="actions"><span class="edit">✎ Edit</span><span class="delete">■ Delete</span></div><div class="dur">3h</div><div class="date">December 9th</div></div>
          </div>
          <div class="task">
            <div><span class="tag">Project Management</span><div class="task-name">Customer A Project 1</div><div class="task-desc">It tracks your progress from first until now</div></div>
            <div class="task-side"><div class="actions"><span class="edit">✎ Edit</span><span class="delete">■ Delete</span></div><div class="dur">5h</div><div class="date">December 9th</div></div>
          </div>
          <div class="task">
            <div><span class="tag">Coding</span><div class="task-name">Customer A Project 1</div><div class="task-desc">It tracks your progress from first until now</div></div>
            <div class="task-side"><div class="actions"><span class="edit">✎ Edit</span><span class="delete">■ Delete</span></div><div class="dur">4h</div><div class="date">December 9th</div></div>
          </div>
        </div>

        <div class="day">
          <div class="day-head">Monday <small>7H 30M</small></div>
          <div class="task">
            <div><span class="tag">Meeting</span><div class="task-name">Customer B Project 1</div><div class="task-desc">It tracks your progress from first until now</div></div>
            <div class="task-side"><div class="actions"><span class="edit">✎ Edit</span><span class="delete">■ Delete</span></div><div class="dur">2h</div><div class="date">December 9th</div></div>
          </div>
        </div>
      </div>
    </div>
  </div>
</section>

</body>
</html>
```